Stationery Set for new venture capital firm

We need a new set of stationery including letterhead, business cards, envelopes, with compliment slips for our new startup venture capital firm known as Halvora.
We make alternative investments globally and hope to have a worldwide network of offices later.

The stationery should be elegant and not too fussy with the use of too many colors.

Venture Capital

```html
<!DOCTYPE html>
<html lang="en">
<head>
<meta charset="utf-8">
<title>Halvora Stationery Set</title>
<link rel="stylesheet" href="https://fonts.googleapis.com/css2?family=Open+Sans:wght@400;600;700&display=swap">
<style>
  :root {
    --brand-blue: #0a8bd0;
    --paper: #ffffff;
    --backdrop: #ececec;
    --ink: #5b5f63;
    --ink-soft: #8a8f94;
    --ink-dark: #33373a;
    --rule-light: rgba(255,255,255,0.25);
  }
  * { box-sizing: border-box; margin: 0; padding: 0; }
  html, body { width: 1200px; height: 795px; overflow: hidden; }
  body {
    background: var(--backdrop);
    font-family: "Open Sans", Arial, sans-serif;
    color: var(--ink);
    position: relative;
  }
  .piece { position: absolute; box-shadow: 0 2px 6px rgba(0,0,0,0.12); }

  /* wordmark */
  .wordmark { display: flex; align-items: center; gap: 6px; font-weight: 700; letter-spacing: 0.2px; white-space: nowrap; }
  .wordmark__dot { border-radius: 50%; background: currentColor; flex: none; }
  .wordmark--blue { color: var(--brand-blue); }
  .wordmark--white { color: var(--paper); }

  /* business card front */
  .card-front {
    left: 36px; top: 60px; width: 310px; height: 177px;
    background: var(--brand-blue);
    display: flex; flex-direction: column; align-items: center; justify-content: center; gap: 8px;
  }
  .card-front .wordmark { font-size: 26px; }
  .card-front .wordmark__dot { width: 14px; height: 14px; }
  .card-front__web { color: var(--paper); font-size: 7px; opacity: 0.85; }

  /* business card back */
  .card-back {
    left: 36px; top: 256px; width: 310px; height: 177px; background: var(--paper);
  }
  .card-back .wordmark { position: absolute; left: 22px; top: 46px; font-size: 17px; }
  .card-back .wordmark__dot { width: 9px; height: 9px; }
  .card-back__person { position: absolute; left: 150px; top: 28px; }
  .card-back__name { color: var(--brand-blue); font-size: 11px; font-weight: 600; }
  .card-back__role { font-size: 6.5px; color: var(--ink-soft); text-transform: uppercase; letter-spacing: 0.5px; margin-bottom: 8px; }
  .contact-line { font-size: 6.5px; line-height: 1.55; color: var(--ink); white-space: nowrap; }
  .contact-line b { color: var(--brand-blue); font-weight: 600; margin-right: 3px; }
  .card-back__web { position: absolute; left: 22px; bottom: 20px; font-size: 6.5px; color: var(--brand-blue); }
  .card-back__band { position: absolute; left: 0; right: 0; bottom: 10px; height: 3px; background: var(--brand-blue); }

  /* notebook */
  .notebook {
    left: 62px; top: 462px; width: 250px; height: 300px; background: var(--brand-blue);
  }
  .notebook__fold { position: absolute; left: 0; right: 0; top: 150px; height: 1px; background: var(--rule-light); }
  .notebook__fold--v { left: 150px; right: auto; top: 0; bottom: 0; width: 1px; height: auto; }
  .notebook__brand { position: absolute; left: 0; right: 0; top: 110px; display: flex; flex-direction: column; align-items: center; gap: 6px; }
  .notebook .wordmark { font-size: 24px; }
  .notebook .wordmark__dot { width: 12px; height: 12px; }
  .notebook__web { color: var(--paper); font-size: 7px; opacity: 0.85; }
  .notebook__spiral { position: absolute; left: -7px; top: 8px; }

  /* letterhead */
  .letterhead {
    left: 384px; top: 46px; width: 494px; height: 700px; background: var(--paper);
    padding: 50px 52px 0 58px;
  }
  .letterhead .wordmark { font-size: 22px; margin-bottom: 46px; }
  .letterhead .wordmark__dot { width: 11px; height: 11px; }
  .letter__greeting { font-size: 9px; font-weight: 700; color: var(--ink-dark); margin-bottom: 12px; }
  .letter__body p { font-size: 8.5px; line-height: 1.65; margin-bottom: 12px; color: var(--ink); }
  .letter__signature { width: 120px; height: 34px; margin-top: 16px; background: linear-gradient(90deg, #e7e8ea, #f2f3f4); border-radius: 2px; }
  .letter__signer { font-size: 8px; font-weight: 700; color: var(--ink-dark); margin-top: 4px; }
  .letter__footer {
    position: absolute; left: 58px; right: 52px; bottom: 34px;
    display: flex; justify-content: space-between; align-items: flex-end;
  }
  .letter__footer .contact-line { font-size: 7px; }
  .letter__footer .link { color: var(--brand-blue); }
  .letter__band { position: absolute; left: 0; right: 0; bottom: 16px; height: 4px; background: var(--brand-blue); }

  /* compliment slip */
  .slip {
    left: 900px; top: 596px; width: 270px; height: 140px; background: var(--paper);
  }
  .slip .wordmark { position: absolute; left: 18px; top: 16px; font-size: 16px; }
  .slip .wordmark__dot { width: 8px; height: 8px; }
  .slip__contacts {
    position: absolute; left: 18px; right: 16px; top: 48px;
    display: flex; justify-content: space-between;
  }
  .slip__contacts .contact-line { font-size: 5.5px; }
  .slip__contacts .link { color: var(--brand-blue); }
  .slip__title { position: absolute; left: 18px; bottom: 22px; font-size: 15px; color: var(--brand-blue); }
  .slip__band { position: absolute; left: 0; right: 0; bottom: 10px; height: 4px; background: var(--brand-blue); }
</style>
</head>
<body>

  <section class="piece card-front">
    <div class="wordmark wordmark--white"><span class="wordmark__dot"></span>Halvora</div>
    <div class="card-front__web">www.halvoragroup.com</div>
  </section>

  <section class="piece card-back">
    <div class="wordmark wordmark--blue"><span class="wordmark__dot"></span>Halvora</div>
    <div class="card-back__person">
      <div class="card-back__name">Lena Marwick</div>
      <div class="card-back__role">Manager</div>
      <div class="contact-line"><b>t</b>+00 2345 6789</div>
      <div class="contact-line"><b>f</b>+00 2345 6790</div>
      <div class="contact-line"><b>e</b>hello@halvoragroup.com</div>
      <div class="contact-line"><b>a</b>12th Floor, Meridian House</div>
      <div class="contact-line">8 Quay Road, Port Lenna</div>
    </div>
    <div class="card-back__web">www.halvoragroup.com</div>
    <div class="card-back__band"></div>
  </section>

  <section class="piece notebook">
    <div class="notebook__fold"></div>
    <div class="notebook__fold notebook__fold--v"></div>
    <svg class="notebook__spiral" width="16" height="284" viewBox="0 0 16 284" aria-hidden="true">
      <g fill="none" stroke="#555a5e" stroke-width="1.6">
        <ellipse cx="8" cy="4" rx="6" ry="2.5"/><ellipse cx="8" cy="15" rx="6" ry="2.5"/>
        <ellipse cx="8" cy="26" rx="6" ry="2.5"/><ellipse cx="8" cy="37" rx="6" ry="2.5"/>
        <ellipse cx="8" cy="48" rx="6" ry="2.5"/><ellipse cx="8" cy="59" rx="6" ry="2.5"/>
        <ellipse cx="8" cy="70" rx="6" ry="2.5"/><ellipse cx="8" cy="81" rx="6" ry="2.5"/>
        <ellipse cx="8" cy="92" rx="6" ry="2.5"/><ellipse cx="8" cy="103" rx="6" ry="2.5"/>
        <ellipse cx="8" cy="114" rx="6" ry="2.5"/><ellipse cx="8" cy="125" rx="6" ry="2.5"/>
        <ellipse cx="8" cy="136" rx="6" ry="2.5"/><ellipse cx="8" cy="147" rx="6" ry="2.5"/>
        <ellipse cx="8" cy="158" rx="6" ry="2.5"/><ellipse cx="8" cy="169" rx="6" ry="2.5"/>
        <ellipse cx="8" cy="180" rx="6" ry="2.5"/><ellipse cx="8" cy="191" rx="6" ry="2.5"/>
        <ellipse cx="8" cy="202" rx="6" ry="2.5"/><ellipse cx="8" cy="213" rx="6" ry="2.5"/>
        <ellipse cx="8" cy="224" rx="6" ry="2.5"/><ellipse cx="8" cy="235" rx="6" ry="2.5"/>
        <ellipse cx="8" cy="246" rx="6" ry="2.5"/><ellipse cx="8" cy="257" rx="6" ry="2.5"/>
        <ellipse cx="8" cy="268" rx="6" ry="2.5"/><ellipse cx="8" cy="279" rx="6" ry="2.5"/>
      </g>
    </svg>
    <div class="notebook__brand">
      <div class="wordmark wordmark--white"><span class="wordmark__dot"></span>Halvora</div>
      <div class="notebook__web">www.halvoragroup.com</div>
    </div>
  </section>

  <section class="piece letterhead">
    <div class="wordmark wordmark--blue"><span class="wordmark__dot"></span>Halvora</div>
    <div class="letter__greeting">Dear Partner,</div>
    <div class="letter__body">
      <p>Thank you for your interest in our firm. We invest across regions and sectors, working closely with founders to build companies that last. This letter sets out how we plan to support your next stage of growth.</p>
      <p>Our team brings long experience in alternative investments, and our partners will remain available to you at every step. We value clear terms, steady guidance and honest reporting.</p>
      <p>Please find the proposed schedule enclosed. We would welcome a meeting next month to review the details together and agree on the first milestones.</p>
      <p>We look forward to working with you.</p>
    </div>
    <div class="letter__signature" role="img" aria-label="Handwritten signature of the company director"></div>
    <div class="letter__signer">Company Director</div>
    <div class="letter__footer">
      <div>
        <div class="contact-line"><b>t</b>+00 2345 6789</div>
        <div class="contact-line"><b>f</b>+00 2345 6790</div>
      </div>
      <div>
        <div class="contact-line">12th Floor, Meridian House</div>
        <div class="contact-line">8 Quay Road, Port Lenna</div>
      </div>
      <div>
        <div class="contact-line">hello@halvoragroup.com</div>
        <div class="contact-line link">www.halvoragroup.com</div>
      </div>
    </div>
    <div class="letter__band"></div>
  </section>

  <section class="piece slip">
    <div class="wordmark wordmark--blue"><span class="wordmark__dot"></span>Halvora</div>
    <div class="slip__contacts">
      <div>
        <div class="contact-line"><b>t</b>+00 2345 6789</div>
        <div class="contact-line"><b>f</b>+00 2345 6790</div>
      </div>
      <div>
        <div class="contact-line">12th Floor, Meridian House</div>
        <div class="contact-line">8 Quay Road, Port Lenna</div>
      </div>
      <div>
        <div class="contact-line">hello@halvoragroup.com</div>
        <div class="contact-line link">www.halvoragroup.com</div>
      </div>
    </div>
    <div class="slip__title">With compliments</div>
    <div class="slip__band"></div>
  </section>

</body>
</html>
```